Velvet Hounds Website - Boutique online pet store for both owners, their homes and their dogs

I need a high end online store for the sale of dog products (collars, leashes, coats etc), products for their owners (pyjamas, cosmetic bags, pencil cases, gift wrapping paper, greeting cards etc) and the owners home (ring holders, cushion covers, throws etc).

Please peruse the following website for a vauge idea of slightly similar stores:

Mybeaglecorner.example.com.au
Pawtrailhub.example.com.au
Terriertreats.example.com.au
Tallpup.example.co.za

Please keep in mind these are breed specific sites. I intend for the business to sell to trending dog breeds, for example, currently in Australia, French Bulldogs and Dachshunds are trending; therefore this will be the business's current focus.

I also intend for this website to be more elegant and refined than the websites mentioned above. Similar to top names brands, with a hint of cuteness to appeal to the animal lover within customers.

Target Market(s)

Velvet Hounds' target market is majority females, late 20's - 40's, either single, in a relationship, or with children who have left the home. They own small and pampered dogs and treat these dogs like their children. They will have a high disposable income.

I want the brand to attract elitist clientele. Comment has been made that people mightn't be able to spell Velvet when searching for the website; those are not the type of customers I want to attract. I think it may be difficult to encapsulate these two target ideas into the brand; I'd like is to appeal to both the 'Melbourne Socialite' and the Noosa stereotype of "I'm too cool to show it, but I really care what you think"

The products will be, for the most part, unique to the market, a few examples include:

custom hand made collars and leads reflecting current human fashion trends;
leather coats for dogs;
flannel pyjamas for dog;
chef's hats for dogs;
furniture which incorporates dogs beds (blanket box, coffee table, bedside table)
bags, cushions, throw rugs, pyjamas made from various dog print fabrics;
fine leather handbags and purses with various and discreet dog themed embellishments;
custom gift wrapping paper etc etc

Amazing customer service and high quality are two of the core values of Velvet Hounds.

The business will be run through the website as well as high-end markets around Brisbane, Gold Coast and Sunshine Coast.

Colors
eea4c8
ffffff
e34197

Requirements
Must have
• MUST BE FULLY OPERATIONAL ON COMPLETION. I own the domain name www.velvethounds.example.com.au. Needs to be functioning on this domain with an operational online store using PayPal.
• Must also be mobile friendly.
• Pages:
• For your pup (shopping page)
• For your home (shopping page)
• For you (shopping page)
• Stationery
• Contact us
• I am open to better and more creative page names.
• MUST have an easy to operate back end that I can use to update products as and when required.

```html
<!DOCTYPE html>
<html lang="en">
<head>
<meta charset="utf-8">
<title>Velvet Hounds – Womens</title>
<link rel="stylesheet" href="https://fonts.googleapis.com/css2?family=Arimo:ital,wght@0,400;0,700;1,400&family=Tinos&display=swap">
<style>
:root{
  --pink:#e34197;
  --pink-soft:#eea4c8;
  --white:#ffffff;
  --page:#ececec;
  --column:#e6e6e6;
  --ink:#333333;
  --muted:#6d6d6d;
  --price:#e8a634;
  --teal:#1f4a4f;
  --mint:#a9dcd6;
  --mint-ink:#3c8f87;
  --footer:#232323;
  --footer-edge:#000000;
  --rule:#c9c9c9;
}
*{box-sizing:border-box;margin:0;padding:0}
html,body{width:970px;height:1200px;overflow:hidden}
body{position:relative;background:var(--page);font-family:"Arimo",Arial,sans-serif;color:var(--ink)}
.side-band{position:absolute;left:0;width:970px;top:106px;height:33px;background:var(--pink-soft)}
.column{position:absolute;left:118px;top:0;width:771px;height:1020px;background:var(--column);box-shadow:0 0 6px rgba(0,0,0,.12)}
.brand{position:absolute;left:0;width:771px;top:28px;text-align:center}
.brand-mark{display:block;width:44px;height:44px;margin:0 auto 10px;background:var(--pink)}
.brand-name{font-size:15px;font-weight:700;letter-spacing:1px;color:var(--teal);text-transform:uppercase}
.nav{position:absolute;left:0;top:128px;width:771px;height:35px;background:var(--pink-soft)}
.nav a{position:absolute;top:11px;font-size:13px;color:var(--white);text-decoration:none;text-transform:uppercase}
.nav .current{border-bottom:1px solid var(--white);padding-bottom:1px}
.cart-icon{position:absolute;left:593px;top:10px}
.section-rule{position:absolute;left:12px;width:750px;height:2px;background:var(--rule)}
.section-tab{position:absolute;left:29px;width:142px;height:29px;background:var(--pink);color:var(--white);font-size:13px;line-height:29px;text-align:center;text-transform:uppercase}
.product{position:absolute;width:142px}
.product .photo{width:142px;height:143px;border:1px solid #cfcfcf;background:var(--white);padding:4px}
.product .photo div{width:100%;height:100%}
.product .meta{display:flex;justify-content:space-between;margin-top:7px;font-size:12px}
.product .name{color:var(--muted)}
.product .price{color:var(--price)}
.similar .price{color:var(--pink)}
.quick{margin-top:9px;font-size:11px;font-style:italic;color:#8a8a8a}
.actions{margin-top:5px;display:flex;gap:3px;font-size:10.5px;font-style:italic}
.btn-cart{background:var(--pink);color:var(--white);padding:1px 4px}
.btn-wish{background:var(--mint);color:var(--mint-ink);padding:1px 4px}
.page-rule{position:absolute;left:0;top:983px;width:970px;height:1px;background:var(--rule)}
.footer{position:absolute;left:0;top:1020px;width:970px;height:180px;background:var(--footer-edge)}
.footer-inner{position:absolute;left:118px;top:0;width:771px;height:180px;background:var(--footer)}
.footer-band{position:absolute;left:118px;top:998px;width:771px;height:30px;background:var(--pink-soft)}
.footer h3{position:absolute;top:24px;font-size:11px;font-weight:400;color:var(--pink);text-transform:uppercase}
.footer h3.social-title{color:var(--white)}
.footer ul{position:absolute;top:43px;list-style:none;font-size:11px;line-height:15px;color:var(--white)}
.social{position:absolute;top:45px;left:610px;display:flex;gap:15px}
.social span{width:34px;height:34px;border-radius:50%;background:var(--white)}
.copyright{position:absolute;left:0;width:771px;top:144px;text-align:center;font-family:"Tinos",Georgia,serif;font-size:9px;color:var(--white)}
</style>
</head>
<body>
<div class="side-band"></div>
<main class="column">
  <header class="brand">
    <span class="brand-mark"></span>
    <span class="brand-name">Velvet Hounds</span>
  </header>

  <nav class="nav">
    <a class="current" style="left:19px">Home</a>
    <a style="left:78px">Puppies</a>
    <a style="left:152px">Mens</a>
    <a style="left:210px">Womens</a>
    <a style="left:288px">Stationery</a>
    <a style="left:383px">Contact Us</a>
    <a style="left:548px">Cart</a>
    <svg class="cart-icon" width="16" height="14" viewBox="0 0 16 14" fill="none" stroke="#fff" stroke-width="1.4"><path d="M1 2h2.5l2 7h7l2-5H5"/><circle cx="6.5" cy="12" r="1.2"/><circle cx="11.5" cy="12" r="1.2"/></svg>
    <a style="left:641px">Login | Signup</a>
  </nav>

  <div class="section-rule" style="top:208px"></div>
  <div class="section-tab" style="top:194px">Womens</div>

  <article class="product" style="left:29px;top:243px"><div class="photo"><div role="img" aria-label="Teal apron with dog print" style="background:linear-gradient(#f4f4f4,#1f5f63 30%,#1a5155)"></div></div><div class="meta"><span class="name">Hukbalahap Boots</span><span class="price">$8.50</span></div><p class="quick">Quick Shop</p><div class="actions"><span class="btn-cart">Add to Cart</span><span class="btn-wish">Add to Wishlist</span></div></article>
  <article class="product" style="left:225px;top:243px"><div class="photo"><div role="img" aria-label="Dark clutch with white dog pattern" style="background:radial-gradient(ellipse 60% 35% at 50% 50%,#3a2a28 90%,#fafafa 100%)"></div></div><div class="meta"><span class="name">Women's Clutch</span><span class="price">$8.50</span></div><p class="quick">Quick Shop</p><div class="actions"><span class="btn-cart">Add to Cart</span><span class="btn-wish">Add to Wishlist</span></div></article>
  <article class="product" style="left:422px;top:243px"><div class="photo"><div role="img" aria-label="Grey shopper bag carried outdoors" style="background:linear-gradient(#6f7f66,#c9c7c2 45%,#3a3a3a)"></div></div><div class="meta"><span class="name">Shopper Bag</span><span class="price">$8.50</span></div><p class="quick">Quick Shop</p><div class="actions"><span class="btn-cart">Add to Cart</span><span class="btn-wish">Add to Wishlist</span></div></article>
  <article class="product" style="left:618px;top:243px"><div class="photo"><div role="img" aria-label="Beige backpack with colourful dog print" style="background:radial-gradient(ellipse 45% 48% at 50% 52%,#e7c7a0 88%,#fafafa 100%)"></div></div><div class="meta"><span class="name">Backpack</span><span class="price">$8.50</span></div><p class="quick">Quick Shop</p><div class="actions"><span class="btn-cart">Add to Cart</span><span class="btn-wish">Add to Wishlist</span></div></article>

  <article class="product" style="left:29px;top:496px"><div class="photo"><div role="img" aria-label="Pink slippers with dog silhouette" style="background:radial-gradient(ellipse 45% 48% at 50% 50%,#e3a4a6 88%,#fafafa 100%)"></div></div><div class="meta"><span class="name">Hukbalahap Boots</span><span class="price">$8.50</span></div><p class="quick">Quick Shop</p><div class="actions"><span class="btn-cart">Add to Cart</span><span class="btn-wish">Add to Wishlist</span></div></article>
  <article class="product" style="left:225px;top:496px"><div class="photo"><div role="img" aria-label="Canvas tote bag with dog print" style="background:radial-gradient(ellipse 38% 42% at 50% 58%,#e4d08a 88%,#fafafa 100%)"></div></div><div class="meta"><span class="name">Canvas Bag</span><span class="price">$8.50</span></div><p class="quick">Quick Shop</p><div class="actions"><span class="btn-cart">Add to Cart</span><span class="btn-wish">Add to Wishlist</span></div></article>
  <article class="product" style="left:422px;top:496px"><div class="photo"><div role="img" aria-label="Pair of grey and blue dog print socks" style="background:linear-gradient(100deg,#fafafa 15%,#cfcfcf 25%,#c6c6c6 48%,#6c7a92 55%,#5d6b84 78%,#fafafa 88%)"></div></div><div class="meta"><span class="name">Hot Dog Socks</span><span class="price">$8.50</span></div><p class="quick">Quick Shop</p><div class="actions"><span class="btn-cart">Add to Cart</span><span class="btn-wish">Add to Wishlist</span></div></article>
  <article class="product" style="left:618px;top:496px"><div class="photo"><div role="img" aria-label="Teal Christmas apron" style="background:linear-gradient(#f4f4f4,#1f5f63 30%,#1a5155)"></div></div><div class="meta"><span class="name">Christmas Apron</span><span class="price">$8.50</span></div><p class="quick">Quick Shop</p><div class="actions"><span class="btn-cart">Add to Cart</span><span class="btn-wish">Add to Wishlist</span></div></article>

  <div class="section-rule" style="top:768px"></div>
  <div class="section-tab" style="top:753px">Similar Items</div>

  <article class="product similar" style="left:17px;top:802px"><div class="photo"><div role="img" aria-label="Pair of dog print socks" style="background:linear-gradient(100deg,#fafafa 15%,#cfcfcf 25%,#c6c6c6 48%,#6c7a92 55%,#5d6b84 78%,#fafafa 88%)"></div></div><div class="meta"><span class="name">Hukbalahap Boots</span><span class="price">$8.50</span></div></article>
  <article class="product similar" style="left:213px;top:802px"><div class="photo"><div role="img" aria-label="Pair of dog print socks" style="background:linear-gradient(100deg,#fafafa 15%,#cfcfcf 25%,#c6c6c6 48%,#6c7a92 55%,#5d6b84 78%,#fafafa 88%)"></div></div><div class="meta"><span class="name">Hukbalahap Boots</span><span class="price">$8.50</span></div></article>
  <article class="product similar" style="left:410px;top:802px"><div class="photo"><div role="img" aria-label="Pair of dog print socks" style="background:linear-gradient(100deg,#fafafa 15%,#cfcfcf 25%,#c6c6c6 48%,#6c7a92 55%,#5d6b84 78%,#fafafa 88%)"></div></div><div class="meta"><span class="name">Hukbalahap Boots</span><span class="price">$8.50</span></div></article>
  <article class="product similar" style="left:606px;top:802px"><div class="photo"><div role="img" aria-label="Pair of dog print socks" style="background:linear-gradient(100deg,#fafafa 15%,#cfcfcf 25%,#c6c6c6 48%,#6c7a92 55%,#5d6b84 78%,#fafafa 88%)"></div></div><div class="meta"><span class="name">Hukbalahap Boots</span><span class="price">$8.50</span></div></article>
</main>

<div class="page-rule"></div>
<footer class="footer">
  <div class="footer-inner">
    <h3 style="left:19px">Links</h3>
    <ul style="left:19px"><li>Home</li><li>Mens</li><li>Womens</li><li>Stationary</li><li>Contact Us</li></ul>
    <h3 style="left:354px">On Sale Items</h3>
    <ul style="left:363px"><li>Lorem ipsum</li><li>Lorem Ipsum</li><li>Lorem Ipsum</li><li>Lorem Ipsum</li></ul>
    <h3 class="social-title" style="left:610px">Get Social With Us!</h3>
    <div class="social" aria-label="Social links"><span></span><span></span><span></span></div>
    <p class="copyright">© Copyright © 2017. Velvet Hounds all rights reserved.</p>
  </div>
</footer>
<div class="footer-band"></div>
</body>
</html>
```